Medical Services Banner Set Project - revised

We need 3 standard size banner sets for each of two medical specialties: bariatric weight loss surgery and plastic surgery.
Our preference is for 3 versions of each set.
1. Interactive flash banner
2. Animated flash banner
3. Static banner
The theme is transition from ugly to beautiful and from fat to thin In looking at other similar banners we believe the key to proper execution is the rendering of the body transition.This is quite difficult to achieve - I have seen multiple attempts and no one can seem to get it just right (realistic and credible).
Action script for interactive banner begins with “before” image, click initiates the action script and image morphs into “after” image (beautiful/thin/sexy)
Animated is same but not interactive, transition on slow loop
Static version uses the” after” image only
Tags lines are respectively:
Stop Dieting and Start Living! (weight loss surgery)
Discover the New You! (plastic surgery)
Sizes:
300x250
728x90
160x600
Name of Company: Corvel Bariatric and Tamsen Cosmetic Surgery
Logo is attached - please do not use tag line

```html
<!DOCTYPE html>
<html lang="en">
<head>
<meta charset="utf-8">
<title>Halvern Bariatric and Tamsen Cosmetic Surgery – Banners</title>
<link rel="stylesheet" href="https://fonts.googleapis.com/css2?family=Arimo:wght@400;700&family=Open+Sans:wght@700&display=swap">
<style>
  :root {
    --page: #ffffff;
    --frame: #1a1a1a;
    --blue-light: #16b4ea;
    --blue-mid: #0a9fdc;
    --blue-deep: #0a87c8;
    --grey-band-light: #f4f4f4;
    --grey-band-dark: #dcdcdc;
    --grey-text: #6b6b6b;
    --accent-blue: #1a9ad6;
    --dark-text: #2b2b2b;
    --logo-navy: #1f4f7d;
    --photo-skin: #d9b29a;
    --photo-grey: #dedede;
    --glove: #e8eef2;
    --white: #ffffff;
  }
  * { margin: 0; padding: 0; box-sizing: border-box; }
  html, body {
    width: 1200px; height: 1000px; overflow: hidden;
    background: var(--page);
    font-family: "Arimo", Arial, sans-serif;
  }
  .canvas { position: relative; width: 1200px; height: 1000px; }

  .banner {
    position: absolute; left: 239px; width: 728px; height: 90px;
    border: 1px solid var(--frame); overflow: hidden;
  }

  /* Cosmetic surgery banner */
  .banner--cosmetic { top: 293px; background: linear-gradient(180deg, var(--blue-light), var(--blue-mid) 55%, var(--blue-deep)); }
  .banner--cosmetic .photo {
    position: absolute; left: 0; top: 0; width: 181px; height: 88px;
    background: linear-gradient(90deg, var(--photo-grey) 0%, var(--photo-grey) 35%, var(--photo-skin) 60%, #c79b80 100%);
  }
  .banner--cosmetic .start {
    position: absolute; left: 198px; top: 52px;
    color: var(--white); font-weight: 700; font-size: 19px; letter-spacing: 0.5px;
    display: flex; align-items: center; gap: 7px;
  }
  .banner--cosmetic .hand {
    position: absolute; left: 262px; top: 20px; width: 78px; height: 68px;
    background: radial-gradient(ellipse at 55% 60%, var(--glove) 0%, rgba(232,238,242,0.5) 55%, rgba(232,238,242,0) 75%);
  }
  .banner--cosmetic .tagline {
    position: absolute; left: 352px; top: 11px; width: 370px;
    color: var(--white); font-weight: 700; font-size: 32px; line-height: 35px;
    text-align: center; text-shadow: 2px 2px 3px rgba(0,0,0,0.45);
  }

  /* Bariatric banner */
  .banner--bariatric { top: 598px; background: linear-gradient(180deg, var(--grey-band-light), var(--grey-band-dark)); }
  .banner--bariatric .brand {
    position: absolute; left: 12px; top: 24px; display: flex; align-items: center; gap: 8px;
  }
  .brand__mark { width: 26px; height: 26px; border-radius: 50%; background: var(--logo-navy); }
  .brand__name {
    color: var(--logo-navy); font-size: 17px; line-height: 19px; font-weight: 400; letter-spacing: 0.5px;
  }
  .banner--bariatric .photo {
    position: absolute; left: 158px; top: 0; width: 157px; height: 88px;
    background: linear-gradient(90deg, #c9a087 0%, var(--photo-skin) 25%, #e3c2ad 55%, #c79b80 100%);
  }
  .headline { font-weight: 700; font-size: 24px; letter-spacing: 2px; white-space: nowrap; }
  .headline__grey { position: absolute; left: 331px; top: 3px; color: var(--grey-text); }
  .headline__blue { position: absolute; left: 517px; top: 3px; color: var(--accent-blue); word-spacing: 6px; }
  .banner--bariatric .subline {
    position: absolute; left: 330px; top: 28px; width: 360px; text-align: center;
    font-family: "Open Sans", Arial, sans-serif; font-weight: 700; font-size: 11px; color: var(--dark-text);
  }
  .banner--bariatric .cta {
    position: absolute; left: 412px; top: 47px; width: 186px; height: 31px;
    background: linear-gradient(180deg, #56c2ea, #1f9fd6);
    box-shadow: 3px 4px 5px rgba(0,0,0,0.3);
    color: var(--white); font-weight: 700; font-size: 16px; letter-spacing: 1.6px;
    display: flex; align-items: center; justify-content: center;
    text-shadow: 1px 1px 2px rgba(0,0,0,0.35);
  }
</style>
</head>
<body>
<div class="canvas">

  <section class="banner banner--cosmetic" aria-label="Tamsen Cosmetic Surgery banner">
    <div class="photo" role="img" aria-label="Photo of a woman's torso in a black bra, before surgery"></div>
    <div class="start">START
      <svg width="14" height="16" viewBox="0 0 14 16" aria-hidden="true"><path d="M0 0 L14 8 L0 16 Z" fill="#ffffff"/></svg>
    </div>
    <div class="hand" role="img" aria-label="Illustration of a gloved hand holding a scalpel"></div>
    <h2 class="tagline">DISCOVER THE NEW YOU!</h2>
  </section>

  <section class="banner banner--bariatric" aria-label="Halvern Bariatric banner">
    <div class="brand">
      <span class="brand__mark"></span>
      <span class="brand__name">HALVERN<br>BARIATRIC</span>
    </div>
    <div class="photo" role="img" aria-label="Photo of a slim woman's torso in a black bra, after weight loss"></div>
    <h2 class="headline"><span class="headline__grey">PERMANENT</span><span class="headline__blue">WEIGHT LOSS</span></h2>
    <p class="subline">SAFE AND AFFORDABLE</p>
    <div class="cta">FIND OUT HOW</div>
  </section>

</div>
</body>
</html>
```